New Branding Business Card Design

Redesign business card according to new branding update.

** The design received so far are single color + BLACK.
I'd encourage designer to use different tones of blue / purple as described in the Designer Brief color palette

Target Market(s)

International

Industry/Entity Type

Medical Equipment

Contact Information for Business Card

Logo on one side (Designer can decide if they want to move certain info from the other side to save space)

Main body info (company name, individual name in both English and Chinese, contact info etc) on the other
Prefer a 'cleaner' layout - vs 'all over the place'
Prefer flush left alignment

Font styles to use
Sans Serif

Requirements
Must have
• Key info
• (Company name (English)): VORAK (HK) Limited
• (Name (English)): Martin L. Osei
• (Credential): FCPA, FHKSI
• (Title): Founder, Managing Director & CEO
• For the following info, designers decide whether to use colon or no colon, stroke separator, or use icon gfx for T (for telephone fixed line, M for mobile etc.)
• T: +852 2741 VORAK / +852 2741 5317
• M: +852 9473 6215 / + 86 139 4527 3916
• E: martin.l.osei@vorak-example.hk
Nice to have
• Depending on the space and spacing available designers can add or use fuller title and other info
• Title: Chairman of the Executive Committee, Founder, Managing Director & CEO
• (Name (Chinese)): 梁文浩
Should not have
• One of our business entities a long company name that cannot be broken into 2 lines
• makes vertical implementation almost impossible

```html
<!DOCTYPE html>
<html lang="en">
<head>
<meta charset="utf-8">
<title>VORAK (HK) Limited — Business Card</title>
<link rel="stylesheet" href="https://fonts.googleapis.com/css2?family=Arimo:wght@400;700&family=Noto+Sans+TC:wght@700&display=swap">
<style>
  :root {
    --bg: #d9dadd;
    --paper: #ffffff;
    --purple: #4f1f78;
    --purple-deep: #46196b;
    --purple-tile: #55267e;
    --ink: #1d1d22;
    --rule: #5a2a86;
  }
  * { box-sizing: border-box; margin: 0; padding: 0; }
  html, body { width: 1200px; height: 800px; overflow: hidden; }
  body {
    background: var(--bg);
    font-family: "Arimo", Arial, sans-serif;
    color: var(--ink);
  }
  .canvas {
    width: 1200px; height: 800px;
    display: flex; flex-direction: column;
    align-items: center; justify-content: center;
    gap: 34px;
  }
  .card {
    position: relative;
    width: 620px; height: 354px;
    border-radius: 2px;
    box-shadow: 0 2px 8px rgba(0,0,0,.18);
    overflow: hidden;
  }

  /* Back side */
  .card--back { background: var(--purple); }
  .card__pattern {
    position: absolute; inset: 10px;
    background: linear-gradient(135deg, var(--purple-tile), var(--purple-deep));
    border-radius: 2px;
  }
  .brand {
    display: flex; align-items: center; gap: 10px;
    font-family: "Arimo", Arial, sans-serif;
    font-weight: 700;
    letter-spacing: .08em;
  }
  .brand__square { width: 26px; height: 26px; border-radius: 5px; }
  .card--back .brand {
    position: absolute; left: 50%; top: 50%;
    transform: translate(-50%, -50%);
    color: #fff; font-size: 34px;
  }
  .card--back .brand__square { background: #fff; width: 30px; height: 30px; }

  /* Front side */
  .card--front { background: var(--paper); }
  .details {
    position: absolute; left: 44px; top: 52px;
    line-height: 1.25;
  }
  .name-zh {
    font-family: "Noto Sans TC", "Arimo", sans-serif;
    font-weight: 700; font-size: 19px; color: var(--purple);
    letter-spacing: .04em;
  }
  .name-en {
    font-weight: 700; font-size: 19px; color: var(--purple);
    margin-top: 2px;
  }
  .name-en .credentials { font-size: 14px; }
  .title { font-size: 14px; margin-top: 2px; }
  .contacts { list-style: none; margin-top: 14px; font-size: 14px; }
  .contacts li { display: flex; align-items: center; gap: 7px; line-height: 1.3; }
  .contacts svg { width: 12px; height: 12px; flex: none; fill: none; stroke: var(--ink); stroke-width: 1.4; }
  .contacts .icon-phone { fill: var(--ink); stroke: none; }
  .company { margin-top: 12px; font-size: 14px; }
  .company__name { color: var(--purple); }
  .rule {
    position: absolute; left: 318px; right: 40px; top: 172px;
    height: 1.5px; background: var(--rule);
  }
  .card--front .brand {
    position: absolute; right: 40px; top: 64px;
    color: var(--purple); font-size: 30px;
  }
  .card--front .brand__square { background: var(--purple); }
  .website {
    position: absolute; right: 40px; bottom: 34px;
    font-size: 15px; color: var(--purple); letter-spacing: .14em;
  }
</style>
</head>
<body>
<main class="canvas">
  <section class="card card--back" aria-label="Card back">
    <div class="card__pattern" role="img" aria-label="Repeating grid of rounded letter tiles in tonal purple"></div>
    <div class="brand"><span class="brand__square"></span><span class="brand__name">VORAK</span></div>
  </section>

  <section class="card card--front" aria-label="Card front">
    <div class="details">
      <p class="name-zh">梁文浩</p>
      <p class="name-en">Martin L. Osei, <span class="credentials">FCPA, FHKSI</span></p>
      <p class="title">Founder, Managing Director &amp; CEO</p>
      <ul class="contacts">
        <li>
          <svg class="icon-phone" viewBox="0 0 12 12" aria-hidden="true"><path d="M2.4 0.8 4.3 2.7 3.4 4.1c.7 1.7 2 3 3.7 3.8l1.4-.9 1.9 1.9-1.2 1.6C5 10.2 1.5 6.7.9 2z"/></svg>
          +852 2741 VORAK / +852 2741 5317
        </li>
        <li>
          <svg viewBox="0 0 12 12" aria-hidden="true"><rect x="3" y="0.8" width="6" height="10.4" rx="1"/><line x1="5" y1="9.4" x2="7" y2="9.4"/></svg>
          +852 9473 6215 / + 86 139 4527 3916
        </li>
        <li>
          <svg viewBox="0 0 12 12" aria-hidden="true"><rect x="0.8" y="2.2" width="10.4" height="7.6"/><polyline points="0.8,2.2 6,6.6 11.2,2.2"/></svg>
          martin.l.osei@vorak-example.hk
        </li>
      </ul>
      <div class="company">
        <p class="company__name">VORAK (HK) Limited</p>
        <p>Units 210-214, Level 2, Block B, Harbourview Park 5</p>
        <p>58 Harbourview Road, Hong Kong</p>
      </div>
    </div>
    <div class="rule"></div>
    <div class="brand"><span class="brand__square"></span><span class="brand__name">VORAK</span></div>
    <p class="website">www.vorak-example.hk</p>
  </section>
</main>
</body>
</html>
```